Label for wiphe fruit jam

We need a label design for a new, unique product.
It is a fruit jam. It is our invention.
We need an etiquette/label design for our new product ZelvoPuli. It is whiping fruits jam in transparent cup. We will have 3 sorts: mango in bright orange colour, strawberry in bright red colour and wild berries in violet
This fruit jam can be wipping with the mixer.
The overrun is up to 100%.
We need a design for this original product.
We have 3 products: mango, strawberry, wild berries.
We are looking for a fruity design. With strong colors. The design must be such that you want to eat the same product.
The product is for wipped desserts, fruity ice cream, pies.
Whipe it at home with simple kitchen mixer.
The size of the label on the side are: 100x55mm.
On top is round, diameter 80mm
Updates

The size of the label are: 100x55mm.On top is round, diameter 80mm Added Monday, February 13, 2017

Target Market(s)

Private customers, housewives, people who like to cook, make dessert, children who like to make ice themselves, etc.

Industry/Entity Type

Product

Requirements
Must have
• The name of the product is Zelvo Puli.
• Maybe you have a better name for this product?

```html
<!DOCTYPE html>
<html lang="en">
<head>
<meta charset="utf-8">
<title>Zelvo Puli – Natural Jam Labels</title>
<link href="https://fonts.googleapis.com/css2?family=Roboto+Slab:wght@700;900&display=swap" rel="stylesheet">
<style>
  :root {
    --canvas: #f4f4f1;
    --paper: #ffffff;
    --brand: #4a6fa5;
    --sweet-green: #6cb33f;
    --jam-orange: #f39a1e;
    --mango: #e8571e;
    --mango-light: #fbd48a;
    --mango-deep: #f29a3a;
    --straw: #c8262d;
    --straw-light: #f6c6c3;
    --straw-deep: #e0575a;
    --berry: #5b3b8c;
    --berry-light: #d6cbe6;
    --berry-deep: #7a5aa8;
  }
  * { box-sizing: border-box; margin: 0; padding: 0; }
  html, body { width: 1200px; height: 608px; overflow: hidden; }
  body {
    background: var(--canvas);
    font-family: "Roboto Slab", Georgia, serif;
    display: flex;
    justify-content: space-around;
    align-items: center;
    padding: 0 20px;
  }
  .flavour {
    width: 370px;
    display: flex;
    flex-direction: column;
    align-items: center;
    gap: 34px;
  }
  .flavour--mango { --tone: var(--mango); --tone-light: var(--mango-light); --tone-deep: var(--mango-deep); }
  .flavour--straw { --tone: var(--straw); --tone-light: var(--straw-light); --tone-deep: var(--straw-deep); }
  .flavour--berry { --tone: var(--berry); --tone-light: var(--berry-light); --tone-deep: var(--berry-deep); }

  .fruit-pattern {
    position: absolute;
    inset: 0;
    background:
      radial-gradient(circle at 18% 25%, var(--tone-deep) 0 9%, transparent 16%),
      radial-gradient(circle at 82% 22%, var(--tone-deep) 0 8%, transparent 15%),
      radial-gradient(circle at 15% 80%, var(--tone-deep) 0 8%, transparent 15%),
      radial-gradient(circle at 85% 78%, var(--tone-deep) 0 9%, transparent 16%),
      linear-gradient(135deg, var(--paper), var(--tone-light));
    opacity: .85;
  }

  /* Round lid label */
  .lid-label {
    position: relative;
    width: 250px;
    height: 250px;
    border-radius: 50%;
    overflow: hidden;
    background: var(--paper);
    box-shadow: 0 2px 8px rgba(0,0,0,.12);
  }
  .lid-label .badge {
    position: absolute;
    left: 50%; top: 50%;
    transform: translate(-50%, -50%);
    width: 200px;
    height: 150px;
    border-radius: 50%;
    background: var(--paper);
  }

  /* Side wrap label */
  .side-label {
    position: relative;
    width: 370px;
    height: 204px;
    overflow: hidden;
    background: var(--paper);
    border-radius: 46% 46% 4px 4px / 22% 22% 4px 4px;
    box-shadow: 0 2px 8px rgba(0,0,0,.12);
  }
  .side-label .badge {
    position: absolute;
    left: 50%; bottom: 0;
    transform: translateX(-50%);
    width: 200px;
    height: 184px;
    border-radius: 100px 100px 0 0;
    background: var(--paper);
  }

  .badge {
    display: flex;
    flex-direction: column;
    align-items: center;
    justify-content: center;
    gap: 6px;
    text-align: center;
  }
  .brand-name {
    font-weight: 700;
    font-size: 20px;
    color: var(--brand);
    display: flex;
    align-items: center;
    gap: 6px;
  }
  .brand-name::before {
    content: "";
    width: 10px; height: 10px;
    border-radius: 50%;
    background: var(--sweet-green);
  }
  .product-name {
    font-weight: 900;
    font-size: 22px;
    letter-spacing: .5px;
    color: var(--tone);
    text-transform: uppercase;
    white-space: nowrap;
  }
  .sweet-tag {
    background: var(--sweet-green);
    color: var(--paper);
    font-weight: 900;
    font-size: 12px;
    letter-spacing: 1px;
    padding: 1px 14px;
    clip-path: polygon(6% 0, 94% 0, 100% 100%, 0 100%);
  }
  .jam-tag {
    border: 2px solid var(--jam-orange);
    color: var(--jam-orange);
    font-weight: 900;
    font-size: 9px;
    letter-spacing: 1px;
    padding: 1px 10px;
    border-radius: 10px;
    text-transform: uppercase;
  }
</style>
</head>
<body>

  <section class="flavour flavour--mango">
    <div class="lid-label">
      <div class="fruit-pattern" role="img" aria-label="Pattern of mango slices and leaves"></div>
      <div class="badge">
        <span class="brand-name">Zelvo Puli</span>
        <span class="product-name">Mango</span>
        <span class="sweet-tag">SWEET</span>
        <span class="jam-tag">Natural Jam</span>
      </div>
    </div>
    <div class="side-label">
      <div class="fruit-pattern" role="img" aria-label="Pattern of mango slices and leaves"></div>
      <div class="badge">
        <span class="brand-name">Zelvo Puli</span>
        <span class="product-name">Mango</span>
        <span class="sweet-tag">SWEET</span>
        <span class="jam-tag">Natural Jam</span>
      </div>
    </div>
  </section>

  <section class="flavour flavour--straw">
    <div class="lid-label">
      <div class="fruit-pattern" role="img" aria-label="Pattern of whole and halved strawberries"></div>
      <div class="badge">
        <span class="brand-name">Zelvo Puli</span>
        <span class="product-name">Strawberries</span>
        <span class="sweet-tag">SWEET</span>
        <span class="jam-tag">Natural Jam</span>
      </div>
    </div>
    <div class="side-label">
      <div class="fruit-pattern" role="img" aria-label="Pattern of whole and halved strawberries"></div>
      <div class="badge">
        <span class="brand-name">Zelvo Puli</span>
        <span class="product-name">Strawberries</span>
        <span class="sweet-tag">SWEET</span>
        <span class="jam-tag">Natural Jam</span>
      </div>
    </div>
  </section>

  <section class="flavour flavour--berry">
    <div class="lid-label">
      <div class="fruit-pattern" role="img" aria-label="Pattern of blackberries with leaves"></div>
      <div class="badge">
        <span class="brand-name">Zelvo Puli</span>
        <span class="product-name">Wild Berries</span>
        <span class="sweet-tag">SWEET</span>
        <span class="jam-tag">Natural Jam</span>
      </div>
    </div>
    <div class="side-label">
      <div class="fruit-pattern" role="img" aria-label="Pattern of blackberries with leaves"></div>
      <div class="badge">
        <span class="brand-name">Zelvo Puli</span>
        <span class="product-name">Wild Berries</span>
        <span class="sweet-tag">SWEET</span>
        <span class="jam-tag">Natural Jam</span>
      </div>
    </div>
  </section>

</body>
</html>
```